furniture and home contents restoration

I need to list the services that we perform in our studio.
we serve the general public as well as the insurance/ remediation industry

```html
<!DOCTYPE html>
<html lang="en">
<head>
<meta charset="utf-8">
<title>Keystone Refinishers – Business Card</title>
<link href="https://fonts.googleapis.com/css2?family=PT+Serif:wght@400;700&display=swap" rel="stylesheet">
<style>
  :root {
    --backdrop: #d3d3cf;
    --card: #1f313c;
    --card-edge: #2f4a58;
    --ink: #ffffff;
    --ink-soft: #e4e8ea;
  }
  * { box-sizing: border-box; margin: 0; padding: 0; }
  html, body {
    width: 1200px; height: 801px; overflow: hidden;
    background: var(--backdrop);
    font-family: "PT Serif", Georgia, serif;
    color: var(--ink);
  }
  .stage {
    width: 1200px; height: 801px;
    display: flex; align-items: center; justify-content: center; gap: 40px;
  }
  .card {
    width: 540px; height: 310px;
    background: var(--card);
    border-radius: 18px;
    box-shadow: 0 3px 0 var(--card-edge);
    position: relative;
    padding: 30px 34px;
  }
  .brand-name {
    font-weight: 700; font-size: 36px; letter-spacing: 0.5px; line-height: 1;
  }

  /* front */
  .front .brand-name { margin-bottom: 26px; }
  .front-body { display: flex; align-items: stretch; gap: 18px; }
  .identity { width: 215px; }
  .person-name { font-size: 21px; font-weight: 700; letter-spacing: 1.5px; text-transform: uppercase; margin-bottom: 6px; }
  .tagline { font-size: 12px; letter-spacing: 1px; text-transform: uppercase; line-height: 1.35; color: var(--ink-soft); text-align: center; }
  .divider { width: 1.5px; background: var(--ink); }
  .contact-list { list-style: none; font-size: 13px; line-height: 1.45; color: var(--ink-soft); }
  .contact-list li { display: flex; align-items: center; gap: 7px; }
  .contact-list svg { width: 10px; height: 10px; flex: none; }
  .service-line {
    position: absolute; left: 0; right: 0; bottom: 32px;
    text-align: center; font-size: 24px; letter-spacing: 1.5px; text-transform: uppercase;
  }

  /* back */
  .back { padding: 24px 26px; }
  .back .brand-name { text-align: center; font-size: 34px; margin-bottom: 16px; }
  .service-columns { display: flex; gap: 18px; }
  .service-list { list-style: none; flex: 1; font-size: 9.6px; letter-spacing: 0.4px; text-transform: uppercase; line-height: 1.55; color: var(--ink-soft); }
  .service-list li::before { content: "\2022"; margin-right: 4px; }
  .back-footer {
    position: absolute; left: 0; right: 0; bottom: 22px;
    text-align: center; font-size: 13px; letter-spacing: 0.8px; text-transform: uppercase; line-height: 1.3;
  }
</style>
</head>
<body>
<main class="stage">

  <section class="card front">
    <h1 class="brand-name">Keystone Refinishers</h1>
    <div class="front-body">
      <div class="identity">
        <h2 class="person-name">Daniel Moretti</h2>
        <p class="tagline">Serving the general public<br>and the insurance industry<br>for over 40 years</p>
      </div>
      <div class="divider"></div>
      <ul class="contact-list">
        <li><svg viewBox="0 0 10 10"><path d="M2 1l2 2-1 1.3c.6 1.2 1.5 2.1 2.7 2.7L7 6l2 2-1.3 1.2C4.5 9 1 5.5.8 2.3z" fill="currentColor"/></svg>555 201 4800</li>
        <li><svg viewBox="0 0 10 10"><rect x="2.5" y="1" width="5" height="8" rx="1" fill="none" stroke="currentColor"/></svg>555 309 7124</li>
        <li><svg viewBox="0 0 10 10"><rect x="1" y="4" width="8" height="5" rx="1" fill="none" stroke="currentColor"/><rect x="3" y="1" width="4" height="3" fill="none" stroke="currentColor"/></svg>555 201 4815</li>
        <li><svg viewBox="0 0 10 10"><path d="M5 10C2.5 6.5 2 5.3 2 4a3 3 0 016 0c0 1.3-.5 2.5-3 6z" fill="currentColor"/><circle cx="5" cy="4" r="1" fill="var(--card)"/></svg>12 elm hollow rd. riverton, ny 10500</li>
        <li><svg viewBox="0 0 10 10"><rect x="1" y="2.5" width="8" height="5.5" fill="none" stroke="currentColor"/><path d="M1 2.5l4 3 4-3" fill="none" stroke="currentColor"/></svg>hello@keystonerefinish.com</li>
      </ul>
    </div>
    <p class="service-line">Home Contents Restoration</p>
  </section>

  <section class="card back">
    <h1 class="brand-name">Keystone Refinishers</h1>
    <div class="service-columns">
      <ul class="service-list">
        <li>Furniture repair and restoration</li>
        <li>Art cleaning and remounting</li>
        <li>Art and mirror frame repair</li>
        <li>Chandelier cleaning and restoration</li>
        <li>Document restoration</li>
        <li>Glass, ceramic, and mirror repair</li>
        <li>Hardware repair and restoration</li>
        <li>Kitchen removal and reinstallation</li>
        <li>Lamp cleaning and restoration</li>
        <li>Lamp shade replacement</li>
      </ul>
      <ul class="service-list">
        <li>Metal polishing and restoration</li>
        <li>Odor removal and ozone services</li>
        <li>Photo restoration</li>
        <li>Upholstery cleaning and deodorizing</li>
        <li>In-house upholstery and reupholstery</li>
        <li>Rug cleaning and restoration</li>
        <li>Musical instrument restoration</li>
        <li>Window treatment repair/ restoration</li>
        <li>Leather restoration and replacement</li>
        <li>Piano restoration and repair</li>
      </ul>
    </div>
    <p class="back-footer">On-site inspections and desk review services<br>Assessment reports and estimates for repair and restoration</p>
  </section>

</main>
</body>
</html>
```